Photographer website, needs Facebook design. (updated details in brief.)

Company name Tobin Vesky Photography, looking to add a Facebook design, that is minimalistic, yet powerful. Less is more in my opinion, but what's there is creative, but eye catchy. see example image in files section for a better idea of what I am looking for. I have also added some source files for my logo.

Target Market(s)

local musicians/artists, models/fashion, and business professional looking for headshots or corporate business profile images.

Colors
0655a3
cfdfed
ffffff

Requirements
Must have
• I have added a screen shot of what I am looking for, for everyone to gain a better sense of my vision. Please see the uploaded files below.
Nice to have
• I am really a fan of the example image in the files section below. Something close to that I would be very happy with.
Should not have
• should not have my face on the cover.

```html
<!DOCTYPE html>
<html lang="en">
<head>
<meta charset="utf-8">
<title>Tobin Vesky Photography — Cover</title>
<link rel="stylesheet" href="https://fonts.googleapis.com/css2?family=Josefin+Sans:wght@400;600&family=Montserrat:ital,wght@0,400;0,500;0,600;1,400&display=swap">
<style>
  :root {
    --page-bg: #eceef1;
    --cover-deep: #020d18;
    --cover-mid: #071b2c;
    --cover-edge: #0b2538;
    --photo-warm: #8a6a45;
    --photo-denim: #1f4560;
    --ink-light: #ffffff;
    --accent-cyan: #2cc3d3;
    --accent-yellow: #d8d21d;
    --ink-dark: #111111;
  }
  * { margin: 0; padding: 0; box-sizing: border-box; }
  html, body {
    width: 1200px; height: 683px; overflow: hidden;
    background: var(--page-bg);
  }
  .cover {
    position: absolute;
    left: 40px; top: 134px;
    width: 1120px; height: 414px;
    border-radius: 6px;
    overflow: hidden;
    background: linear-gradient(90deg, var(--cover-deep) 0%, var(--cover-mid) 45%, var(--cover-edge) 100%);
  }
  .cover__portrait {
    position: absolute;
    left: 0; top: 0;
    width: 420px; height: 414px;
    background:
      radial-gradient(ellipse 38% 45% at 52% 42%, rgba(214,170,120,0.55), rgba(214,170,120,0) 70%),
      radial-gradient(ellipse 45% 30% at 55% 90%, var(--photo-denim), rgba(31,69,96,0) 75%),
      radial-gradient(ellipse 55% 70% at 45% 45%, var(--photo-warm), rgba(138,106,69,0) 72%),
      transparent;
    opacity: 0.85;
  }
  .cover__info {
    position: absolute;
    left: 724px; top: 0;
    width: 0;
  }
  .cover__info > * {
    position: absolute;
    left: 0;
    transform: translateX(-50%);
    white-space: nowrap;
    color: var(--ink-light);
    text-align: center;
  }
  .brand__name {
    top: 86px;
    font-family: "Josefin Sans", sans-serif;
    font-weight: 400;
    font-size: 36px;
    letter-spacing: 7px;
    line-height: 1;
  }
  .brand__trade {
    top: 124px;
    font-family: "Montserrat", sans-serif;
    font-weight: 500;
    font-size: 21px;
    letter-spacing: 5px;
    line-height: 1;
  }
  .brand__tagline {
    top: 160px;
    font-family: "Montserrat", sans-serif;
    font-weight: 500;
    font-size: 15px;
    letter-spacing: 2px;
    color: var(--accent-cyan);
    line-height: 1;
  }
  .contact__email, .contact__phone {
    font-family: "Montserrat", sans-serif;
    font-weight: 500;
    font-size: 16px;
    letter-spacing: 1px;
    line-height: 1;
  }
  .contact__email { top: 206px; }
  .contact__phone { top: 230px; }
  .cta {
    top: 265px;
    width: 181px; height: 49px;
    background: var(--accent-yellow);
    color: var(--ink-dark);
    font-family: "Montserrat", sans-serif;
    font-weight: 600;
    font-size: 15px;
    letter-spacing: 2px;
    line-height: 49px;
  }
  .cta__note {
    top: 327px;
    font-family: "Montserrat", sans-serif;
    font-style: italic;
    font-weight: 400;
    font-size: 14.5px;
    letter-spacing: 1px;
    line-height: 1;
  }
</style>
</head>
<body>
  <section class="cover">
    <div class="cover__portrait" role="img" aria-label="Studio portrait of a woman with long blonde hair in a denim shirt, seen in profile against a dark background"></div>
    <div class="cover__info">
      <h1 class="brand__name">TOBIN VESKY</h1>
      <p class="brand__trade">PHOTOGRAPHY</p>
      <p class="brand__tagline">CALGARY PHOTOGRAPHER</p>
      <p class="contact__email">info@tobinvesky.ca</p>
      <p class="contact__phone">+1 (403) 555 0147</p>
      <p class="cta">BOOK NOW</p>
      <p class="cta__note">Starting from $299</p>
    </div>
  </section>
</body>
</html>
```